361191

item 1. 8.5x11 1-side flyer design
item 2. 18x24 1-side poster design (also wants at 8.5x11)
item 3. 11x8.5 2-side brochure
design with Brookvale Healthcare brand standards similar to the job you did under 360565
see all attachments

```html
<!DOCTYPE html>
<html lang="en">
<head>
<meta charset="utf-8">
<title>Syphilis Is On The Rise – Brookvale Healthcare</title>
<link rel="stylesheet" href="https://fonts.googleapis.com/css2?family=Anton&family=Poppins:wght@400;500;600;700&display=swap">
<style>
  :root {
    --teal-dark: #27434f;
    --teal-deep: #1f3a45;
    --sage: #7a9e86;
    --sage-dark: #4c6b58;
    --panel-top: #3f5e4c;
    --panel-bottom: #7d9787;
    --silver-1: #f4efea;
    --silver-2: #b9b0aa;
    --text-grey: #5c5c5c;
    --white: #ffffff;
    --alert-red: #d7262c;
  }
  * { box-sizing: border-box; margin: 0; padding: 0; }
  html, body { width: 927px; height: 1200px; overflow: hidden; background: #fff; }
  .flyer {
    position: relative; width: 927px; height: 1200px; overflow: hidden;
    font-family: "Poppins", sans-serif; background: #fff;
  }
  .backdrop { position: absolute; inset: 0; }

  .tagline-band {
    position: absolute; left: 0; top: 32px; width: 927px; height: 86px;
    background: linear-gradient(90deg, var(--silver-2) 0%, var(--silver-1) 30%, #e8e1dc 70%, var(--silver-2) 100%);
  }
  .tagline {
    position: absolute; left: 249px; top: 42px; width: 660px;
    font-size: 26px; font-weight: 500; line-height: 33px; color: var(--teal-dark);
  }

  .brand-tab {
    position: absolute; left: 42px; top: 0; width: 189px; height: 272px;
    background: #fff; border-radius: 0 0 95px 95px;
    display: flex; flex-direction: column; align-items: center; justify-content: flex-end;
    padding-bottom: 70px; gap: 14px;
  }
  .brand-dot { width: 56px; height: 56px; border-radius: 50%; border: 5px solid var(--teal-dark); }
  .brand-name {
    font-size: 27px; line-height: 28px; font-weight: 500; color: var(--teal-dark);
    text-align: center; letter-spacing: -0.5px;
  }

  .headline { position: absolute; left: 45px; top: 296px; font-family: "Anton", sans-serif; }
  .headline-main { display: block; font-size: 104px; line-height: 100px; color: var(--sage); letter-spacing: 3px; }
  .headline-sub { display: block; font-size: 63px; line-height: 66px; color: var(--white); letter-spacing: 2px; margin-top: 4px; }

  .photo-ring {
    position: absolute; left: 466px; top: 126px; width: 490px; height: 490px; border-radius: 50%;
    border: 12px solid #d8d0ca;
  }
  .photo {
    position: absolute; left: 497px; top: 156px; width: 430px; height: 430px; border-radius: 50%;
    background: radial-gradient(circle at 35% 30%, #f2bf8f 0%, #e7a978 40%, #eec9b6 70%, #f3f3f3 100%);
  }

  .stages { position: absolute; left: 43px; top: 585px; width: 455px; }
  .stage { position: relative; height: 111px; border: 1.5px solid var(--teal-dark); border-left: none; margin-left: 55px; background: rgba(255,255,255,0.85); }
  .stage + .stage { border-top: none; }
  .stage-num {
    position: absolute; top: 0; width: 56px; height: 111px;
    display: flex; align-items: center; justify-content: center;
    font-size: 30px; font-weight: 400;
  }
  .stage-num.silver { left: -55px; border-radius: 56px 0 0 56px; background: linear-gradient(90deg, #b9b1ab, #f6f3f0 70%, #ddd6d1); color: #111; }
  .stage-num.green { left: 0; border-radius: 0 56px 56px 0; background: linear-gradient(90deg, #3b5b48, #6d8f78); color: #fff; }
  .stage-text { position: absolute; left: 67px; top: 18px; width: 340px; }
  .stage-title { font-size: 22px; font-weight: 600; color: var(--sage); line-height: 30px; }
  .stage-body { font-size: 16.5px; color: var(--text-grey); line-height: 21px; margin-top: 4px; }
  .sep { color: #c4c4c4; padding: 0 2px; }

  .side-panel {
    position: absolute; left: 522px; top: 470px; width: 364px; height: 700px;
    background: linear-gradient(180deg, var(--panel-top) 0%, var(--sage-dark) 45%, var(--panel-bottom) 100%);
  }
  .treatment-title {
    position: absolute; left: 540px; top: 632px; width: 330px; text-align: center;
    font-size: 31px; font-weight: 700; line-height: 33px; color: #fff;
  }
  .vial-photo {
    position: absolute; left: 584px; top: 742px; width: 243px; height: 161px;
    background: linear-gradient(160deg, #2fb6c4 0%, #3dc1cb 50%, #7fd0d5 100%);
  }
  .panel-rule { position: absolute; left: 554px; top: 917px; width: 302px; height: 1.5px; background: #fff; }
  .prevention-title {
    position: absolute; left: 540px; top: 926px; width: 330px; text-align: center;
    font-size: 31px; font-weight: 700; color: var(--teal-dark);
  }
  .prevention-list { position: absolute; left: 568px; top: 980px; width: 300px; list-style: none; }
  .prevention-list li { position: relative; padding-left: 36px; font-size: 23px; line-height: 25px; color: #fff; margin-bottom: 12px; }
  .prevention-list svg { position: absolute; left: 0; top: 3px; }

  .web-pill {
    position: absolute; left: 537px; top: 1123px; width: 337px; height: 36px; border-radius: 18px;
    background: #fff; border: 2px solid #cfc8c3; display: flex; align-items: center;
  }
  .web-icon { width: 48px; height: 36px; border-radius: 18px; background: linear-gradient(90deg,#b9b1ab,#f3efec); display: flex; align-items: center; justify-content: center; margin-left: -2px; }
  .web-url { font-size: 17px; font-weight: 500; color: var(--teal-dark); margin-left: 12px; }

  .cta-band {
    position: absolute; left: 0; top: 1060px; width: 490px; height: 98px;
    background: linear-gradient(90deg, #1f3a45 0%, #4a6656 100%);
  }
  .cta { position: absolute; left: 98px; top: 1062px; font-family: "Anton", sans-serif; }
  .cta-main { display: block; font-size: 46px; line-height: 52px; color: #fff; letter-spacing: 1px; }
  .cta-sub { display: flex; align-items: center; gap: 10px; font-size: 34px; line-height: 38px; color: var(--sage); margin-left: 8px; }
  .cta-sub::before, .cta-sub::after { content: ""; width: 48px; height: 2px; background: var(--sage); }
  .no-needle { position: absolute; left: 356px; top: 1056px; }
</style>
</head>
<body>
<main class="flyer">
  <svg class="backdrop" width="927" height="1200" viewBox="0 0 927 1200" aria-hidden="true">
    <path d="M0 0 H927 V420 C760 520 620 560 520 540 C360 510 200 520 0 470 Z" fill="#27434f"/>
    <path d="M0 470 C200 520 360 510 520 540 C600 556 680 545 760 520 C640 575 520 590 420 585 C240 575 120 540 0 520 Z" fill="#5f826c"/>
    <path d="M0 1165 C300 1150 600 1175 927 1070 V1200 H0 Z" fill="#1f3a45"/>
  </svg>

  <div class="tagline-band"></div>
  <p class="tagline">Just Because The Symptoms Go Away Doesn’t Mean You’re Cured Without Treatment</p>

  <div class="brand-tab">
    <span class="brand-dot"></span>
    <span class="brand-name">Brookvale<br>Healthcare</span>
  </div>

  <h1 class="headline">
    <span class="headline-main">SYPHILIS</span>
    <span class="headline-sub">IS ON THE RISE</span>
  </h1>

  <div class="side-panel"></div>
  <div class="photo-ring"></div>
  <div class="photo" role="img" aria-label="Person touching a red skin rash on the back of the neck"></div>

  <section class="stages">
    <div class="stage">
      <span class="stage-num silver">1</span>
      <div class="stage-text">
        <h2 class="stage-title">Signs Primary Stage</h2>
        <p class="stage-body">Sores called chancres on genitals or mouth</p>
      </div>
    </div>
    <div class="stage">
      <span class="stage-num green">2</span>
      <div class="stage-text">
        <h2 class="stage-title">Signs Seconday Stage</h2>
        <p class="stage-body">Sore Throat <span class="sep">|</span> Weight Loss <span class="sep">|</span> Skin Rashes Joint Pain <span class="sep">|</span> Fever <span class="sep">|</span> Fatigue</p>
      </div>
    </div>
    <div class="stage">
      <span class="stage-num silver">3</span>
      <div class="stage-text">
        <h2 class="stage-title">Latent Stage</h2>
        <p class="stage-body">No Symptoms in Latent Stage</p>
      </div>
    </div>
    <div class="stage">
      <span class="stage-num green">4</span>
      <div class="stage-text">
        <h2 class="stage-title">Signs Tertiary Stage</h2>
        <p class="stage-body">Memory Loss <span class="sep">|</span> Deafness <span class="sep">|</span> Paralysis Neurological problems</p>
      </div>
    </div>
  </section>

  <h2 class="treatment-title">TREATMENT IS EASY IF CAUGHT EARLY</h2>
  <div class="vial-photo" role="img" aria-label="Medicine vial and syringe on a teal background"></div>
  <div class="panel-rule"></div>
  <h2 class="prevention-title">PREVENTION</h2>
  <ul class="prevention-list">
    <li><svg width="22" height="20" viewBox="0 0 22 20"><path d="M2 10 L8 17 L20 3" fill="none" stroke="#fff" stroke-width="3"/></svg>Use Condoms</li>
    <li><svg width="22" height="20" viewBox="0 0 22 20"><path d="M2 10 L8 17 L20 3" fill="none" stroke="#fff" stroke-width="3"/></svg>Avoid Recreational Drugs &amp; Multiple Sex Partners</li>
  </ul>

  <div class="web-pill">
    <span class="web-icon">
      <svg width="24" height="24" viewBox="0 0 24 24" fill="none" stroke="#27434f" stroke-width="1.8"><circle cx="12" cy="12" r="10"/><path d="M2 12 H22 M12 2 C7 7 7 17 12 22 M12 2 C17 7 17 17 12 22"/></svg>
    </span>
    <span class="web-url">www.brookvalehealthcare.net</span>
  </div>

  <div class="cta-band"></div>
  <div class="cta">
    <span class="cta-main">Get Tested</span>
    <span class="cta-sub">Today</span>
  </div>
  <svg class="no-needle" width="106" height="106" viewBox="0 0 106 106" aria-hidden="true">
    <circle cx="53" cy="53" r="48" fill="#fff" stroke="#d7262c" stroke-width="7"/>
    <g stroke="#8aa0a8" stroke-width="3" fill="none">
      <path d="M28 80 L42 66"/>
      <rect x="40" y="38" width="14" height="36" transform="rotate(45 47 56)" fill="#e6eef0"/>
      <path d="M60 44 L74 30 M70 26 L78 34"/>
    </g>
    <path d="M20 20 L86 86" stroke="#d7262c" stroke-width="7"/>
  </svg>
</main>
</body>
</html>
```